Flyer-Design für ambulanten Pflegedienst
Zielgruppe
Wir sind ein ambulanter Pflegedienst in Rostock und in Gnoien. Patienten werden in der Häuslichkeit versorgt.
Aufgabenstellung
Folgender Flyer soll erstellt werden.
Das Format kann vom Designer festgelegt werden:
Ein paar Flyer habe ich mit hochgeladen. Es sollte jedoch einmal ein ganz neues modernes Design sein.
Vorderseite:Text:
Sie kommen mit den alltäglichen Dingen des Lebens
nicht mehr gut alleine zurecht?
Wir unterstützen Sie gerne bei der Beantragung eines
Pflegegrades. Nachdem der Ärztliche Prüfstelle der Versicherer
sich angemeldet hat, begleiten wir Sie bei der Begutachtung.
Rückseite:
Pflegeberatung:
Wenn Sie einen Pflegegrad haben und von einer privaten Pflegeperson
versorgt werden, erwartet Ihre Pflegekasse in regelmäßigen Abständen einen Beratungebesuch
von einem anerkannten Pflegedienst.
Bitte beide Logos vom Pflegehaus Lindental und vom Pflegedienst Kavuro auf den Flyer
Auch beide Adressen auf den Flyer:

```html
<!DOCTYPE html>
<html lang="de">
<head>
<meta charset="utf-8">
<title>Pflegeberatung – Pflegehaus Lindental</title>
<link rel="stylesheet" href="https://fonts.googleapis.com/css2?family=Passion+One:wght@400;700&family=Montserrat:ital,wght@1,400&display=swap">
<style>
  :root {
    --sky-light: #dcedf6;
    --sky-mid: #a9c3e4;
    --slate-blue: #7f9bd2;
    --slate-deep: #6c84b5;
    --band-light: #e4f2f8;
    --band-line: #7b90c6;
    --ink-green: #1f3b28;
    --accent-yellow: #f4ec3a;
    --warm-orange: #f5702a;
    --warm-yellow: #fcd22a;
    --ring-blue: #1aa3e0;
    --name-green: #5aae3a;
  }
  html, body {
    margin: 0;
    padding: 0;
    width: 1200px;
    height: 2218px;
    overflow: hidden;
  }
  .flyer {
    position: relative;
    width: 1200px;
    height: 2218px;
    overflow: hidden;
    background: linear-gradient(118deg, var(--sky-light) 0%, var(--sky-light) 34%, var(--sky-mid) 46%, var(--slate-blue) 58%, var(--slate-deep) 78%, var(--slate-deep) 100%);
  }
  .flyer-shapes {
    position: absolute;
    inset: 0;
    width: 1200px;
    height: 2218px;
  }
  .brand {
    position: absolute;
    left: 624px;
    top: 330px;
    width: 280px;
    text-align: center;
  }
  .brand-mark {
    width: 180px;
    height: 180px;
    margin: 0 auto;
    border: 9px solid var(--ring-blue);
    border-radius: 50%;
    box-sizing: border-box;
  }
  .brand-name {
    margin-top: 10px;
    font-family: "Passion One", sans-serif;
    font-weight: 400;
    font-size: 36px;
    line-height: 1;
    color: var(--name-green);
    white-space: nowrap;
  }
  .advice {
    position: absolute;
    left: 49px;
    top: 550px;
    margin: 0;
    font-family: "Passion One", sans-serif;
    font-weight: 700;
    font-size: 56px;
    line-height: 92px;
    color: var(--ink-green);
  }
  .advice span { display: block; white-space: nowrap; }
  .address {
    position: absolute;
    margin: 0;
    font-family: "Montserrat", sans-serif;
    font-style: italic;
    font-weight: 400;
    font-size: 30px;
    line-height: 56px;
    letter-spacing: 1.5px;
    text-transform: uppercase;
    color: var(--accent-yellow);
  }
  .address span { display: block; white-space: nowrap; }
  .address-rostock { left: 258px; top: 1516px; }
  .address-gnoien { left: 245px; top: 1904px; }
</style>
</head>
<body>
<main class="flyer">
  <svg class="flyer-shapes" viewBox="0 0 1394 2576" preserveAspectRatio="none">
    <defs>
      <linearGradient id="photo-care-left" x1="0" y1="0" x2="1" y2="0">
        <stop offset="0" stop-color="#3d86cf"/>
        <stop offset="0.4" stop-color="#c9b8a3"/>
        <stop offset="1" stop-color="#e9e3d6"/>
      </linearGradient>
      <linearGradient id="photo-care-right" x1="0" y1="0" x2="1" y2="0">
        <stop offset="0" stop-color="#e8d8c6"/>
        <stop offset="0.5" stop-color="#d9b48f"/>
        <stop offset="1" stop-color="#e7a79c"/>
      </linearGradient>
      <clipPath id="photo-area">
        <path d="M0,0 H1394 V205 C1180,180 960,240 760,335 C560,430 280,455 0,385 Z"/>
      </clipPath>
      <linearGradient id="band-line" x1="0" y1="0" x2="1" y2="0">
        <stop offset="0" stop-color="var(--band-line)"/>
        <stop offset="0.55" stop-color="var(--band-line)" stop-opacity="0.8"/>
        <stop offset="1" stop-color="var(--band-line)" stop-opacity="0"/>
      </linearGradient>
      <linearGradient id="warm-ribbon" x1="0" y1="0" x2="1" y2="0">
        <stop offset="0" stop-color="var(--warm-orange)" stop-opacity="0.35"/>
        <stop offset="0.6" stop-color="var(--warm-yellow)" stop-opacity="0.35"/>
        <stop offset="1" stop-color="var(--warm-yellow)" stop-opacity="0.25"/>
      </linearGradient>
    </defs>

    <g clip-path="url(#photo-area)">
      <rect class="photo-left" x="0" y="0" width="716" height="460" fill="url(#photo-care-left)" role="img" aria-label="Foto: Pflegerin im blauen Kittel lacht gemeinsam mit einer älteren Dame im Sessel"/>
      <rect class="photo-right" x="722" y="0" width="672" height="460" fill="url(#photo-care-right)" role="img" aria-label="Foto: Ältere Dame und eine Betreuerin lächeln einander zu"/>
    </g>

    <path class="top-band" d="M0,385 C280,455 560,430 760,335 C960,240 1180,180 1394,205 L1394,300 C1180,270 980,320 800,410 C620,500 330,610 0,520 Z" fill="var(--band-light)"/>
    <path class="top-band-fade" d="M800,410 C980,320 1180,270 1394,300 L1394,360 C1200,320 1000,380 840,460 Z" fill="var(--band-light)" opacity="0.45"/>
    <path class="band-line" d="M5,540 C180,615 420,610 620,520 C760,455 860,420 980,400" fill="none" stroke="url(#band-line)" stroke-width="12" stroke-linecap="round"/>

    <rect class="warm-ribbon" x="0" y="1860" width="1394" height="270" fill="url(#warm-ribbon)" role="img" aria-label="Dekoratives geschwungenes Band in Orange und Gelb"/>
  </svg>

  <div class="brand">
    <div class="brand-mark"></div>
    <div class="brand-name">Pflegehaus Lindental</div>
  </div>

  <p class="advice">
    <span>Pflegeberatung:</span>
    <span>Wenn Sie einen Pflegegrad haben und von</span>
    <span>einer privaten Pflegeperson versorgt werden,</span>
    <span>erwartet Ihre Pflegekasse in regelmäßigen</span>
    <span>Abständen einen Beratungebesuch von einem</span>
    <span>anerkannten Pflegedienst. Vereinbaren Sie</span>
    <span>unter der Telefonnummer</span>
    <span>0800 4417263 rechtzeitig einen Termin,</span>
    <span>damit ihre optimale</span>
    <span>Versorgung weiterhin sichergestellt ist.</span>
  </p>

  <address class="address address-rostock">
    <span>Pflegehaus Lindental GmbH</span>
    <span>Lindenhofweg 14</span>
    <span>18055 Rostock</span>
    <span>Tel 0800 4417263</span>
    <span>www.pflegehaus-lindental.de</span>
  </address>

  <address class="address address-gnoien">
    <span>Kavuro der mobile Pflegedienst GmbH</span>
    <span>Am Wiesengrund 21</span>
    <span>17179 Gnoien</span>
    <span>www.kavuro-pflege.de</span>
  </address>
</main>
</body>
</html>
```